Upscale dog care facility need some marketing material

We offer a lot of services for dogs and their humans. We have a large indoor dog park, swimming pools, dog daycare and boarding, Pet CPR/First Aid classes and training. We love the trifold brochures where we can highlight all of our services (even a few pics of the facility) as well as give everyone information on our pricing and membership concepts. Will primarily be used for marketing to vets and local pet stores to help get the word out about our business.

```html
<!DOCTYPE html>
<html lang="en">
<head>
<meta charset="utf-8">
<title>Dog Daycare Trifold Brochure</title>
<link href="https://fonts.googleapis.com/css2?family=Fredoka:wght@500;600;700&family=Montserrat:wght@300;400;500;600&display=swap" rel="stylesheet">
<style>
  :root {
    --magenta: #c91f80;
    --magenta-dark: #a8166a;
    --yellow: #ece79c;
    --orange: #f2a73b;
    --orange-deep: #ee9a2e;
    --teal: #2aaa8f;
    --teal-dark: #1f8b74;
    --white: #ffffff;
    --ink: #1d1d1d;
    --paper: #ececec;
    --photo-warm: #d9c6b4;
    --photo-cool: #b9c7cf;
    --photo-grass: #6f9f45;
    --photo-soft: #e6e2dc;
  }
  * { box-sizing: border-box; margin: 0; padding: 0; }
  html, body { width: 742px; height: 1200px; overflow: hidden; }
  body {
    background: var(--paper);
    font-family: "Montserrat", Arial, sans-serif;
    position: relative;
  }
  .brochure {
    position: absolute;
    left: 21px;
    width: 700px;
    height: 540px;
    overflow: hidden;
    box-shadow: 0 8px 24px rgba(0,0,0,0.18);
  }
  .brochure--outside { top: 28px; }
  .brochure--inside { top: 632px; }
  .brochure__bg { position: absolute; inset: 0; }
  .abs { position: absolute; }
  .heading {
    font-family: "Fredoka", Arial, sans-serif;
    font-weight: 600;
    line-height: 1.05;
  }
  .body-copy { font-size: 8px; line-height: 1.35; }
  .white { color: var(--white); }
  .magenta { color: var(--magenta); }

  .photo { background: linear-gradient(135deg, var(--photo-warm), var(--photo-cool)); }
  .photo--round { border-radius: 50%; border: 4px solid var(--white); }
  .photo-ring { border-radius: 50%; border: 1.5px dashed var(--white); }
  .blob { border-radius: 48% 52% 46% 54% / 58% 55% 45% 42%; }

  .tick {
    width: 22px; height: 22px; border-radius: 50%;
    background: var(--teal);
    display: flex; align-items: center; justify-content: center;
  }

  /* Outside: features panel */
  .feature-title { left: 20px; top: 38px; width: 200px; font-size: 15px; }
  .feature-text { left: 118px; width: 105px; color: var(--white); }

  /* About panel */
  .about-title { left: 233px; width: 234px; top: 182px; text-align: center; font-size: 22px; }
  .about-text { left: 253px; width: 194px; top: 216px; text-align: center; color: var(--ink); }
  .contact { left: 233px; width: 234px; top: 440px; text-align: center; color: var(--white); font-size: 8px; line-height: 1.6; }
  .contact svg { vertical-align: -1px; margin-right: 3px; }

  /* Cover */
  .cover-title { left: 467px; width: 233px; top: 24px; text-align: center; font-size: 44px; font-weight: 700; color: var(--white); line-height: 0.92; }
  .cover-tagline { left: 467px; width: 233px; top: 338px; text-align: center; font-size: 25px; }
  .cover-rule { left: 490px; width: 187px; top: 410px; height: 1px; background: var(--white); }
  .cover-phone { left: 467px; width: 233px; top: 422px; text-align: center; font-family: "Fredoka", Arial, sans-serif; font-weight: 600; font-size: 30px; color: var(--white); }
  .cover-web { left: 467px; width: 233px; top: 460px; text-align: center; font-size: 10px; letter-spacing: 2px; color: var(--white); font-weight: 500; }

  /* Inside */
  .why-title { left: 22px; top: 232px; font-size: 24px; }
  .why-rule { left: 22px; top: 264px; width: 190px; height: 1px; background: var(--teal); }
  .why-text { left: 22px; top: 272px; width: 195px; color: var(--ink); }

  .quote { color: var(--white); font-size: 7.5px; line-height: 1.35; }
  .quote-mark { font-family: Georgia, serif; font-size: 44px; color: var(--teal-dark); line-height: 1; }
  .quote-author { font-size: 7px; letter-spacing: 0.5px; color: var(--white); }

  .services-title { left: 252px; top: 28px; font-size: 23px; color: var(--white); }
  .services-rule { left: 252px; top: 58px; width: 200px; height: 1px; background: var(--white); }
  .service { left: 252px; width: 205px; height: 62px; display: flex; align-items: center; gap: 12px; border-bottom: 1px solid rgba(255,255,255,0.8); }
  .service .photo { width: 44px; height: 44px; border-radius: 50%; flex: none; }
  .service span { font-size: 14px; font-weight: 400; color: var(--white); line-height: 1.1; }

  .pricing-title { left: 485px; top: 24px; font-size: 21px; color: var(--white); width: 200px; }
  .pricing-rule { left: 485px; top: 74px; width: 200px; height: 1px; background: var(--white); }
  .price-row { left: 485px; width: 205px; }
  .price-tag {
    display: inline-block; background: var(--orange); color: var(--white);
    font-family: "Fredoka", Arial, sans-serif; font-weight: 600; font-size: 20px;
    padding: 1px 12px; border-radius: 4px; vertical-align: middle;
  }
  .price-name { display: inline-block; margin-left: 8px; vertical-align: middle; font-family: "Fredoka", Arial, sans-serif; font-weight: 600; font-size: 14px; color: var(--white); }
  .price-note { font-size: 7px; color: var(--white); line-height: 1.3; margin-top: 3px; }
</style>
</head>
<body>

<!-- Outside spread -->
<section class="brochure brochure--outside">
  <svg class="brochure__bg" width="700" height="540" viewBox="0 0 700 540" aria-hidden="true">
    <rect x="0" y="0" width="233.3" height="540" fill="var(--magenta)"/>
    <rect x="233.3" y="0" width="233.4" height="540" fill="var(--yellow)"/>
    <rect x="466.7" y="0" width="233.3" height="540" fill="var(--teal)"/>
    <path d="M0 380 C70 392 130 436 233.3 418 L233.3 540 L0 540 Z" fill="var(--orange)"/>
    <path d="M0 380 C70 392 130 436 233.3 418" fill="none" stroke="var(--magenta)" stroke-width="1.2" stroke-dasharray="3 3" transform="translate(0 8)"/>
    <path d="M233.3 418 C330 430 410 380 466.7 300 L466.7 540 L233.3 540 Z" fill="var(--orange)"/>
    <path d="M233.3 418 C330 430 410 380 466.7 300" fill="none" stroke="var(--magenta)" stroke-width="1.2" stroke-dasharray="3 3" transform="translate(0 6)"/>
    <path d="M466.7 300 C540 240 620 250 700 222 L700 540 L466.7 540 Z" fill="var(--orange)"/>
    <path d="M466.7 300 C540 240 620 250 700 222" fill="none" stroke="var(--magenta)" stroke-width="1.2" stroke-dasharray="3 3" transform="translate(0 8)"/>
    <circle cx="620" cy="60" r="70" fill="var(--teal-dark)" opacity="0.25"/>
  </svg>

  <!-- Features panel -->
  <h2 class="abs heading white feature-title">Lorem ipsum dolor sit amet, consectetur adipiscing elit</h2>

  <div class="abs photo-ring" style="left:22px;top:96px;width:86px;height:86px;"></div>
  <div class="abs photo photo--round" role="img" aria-label="Veterinarian examining a dog" style="left:30px;top:104px;width:70px;height:70px;"></div>
  <div class="abs tick" style="left:18px;top:108px;"><svg width="12" height="12" viewBox="0 0 12 12"><path d="M2 6.5 L5 9 L10 3" stroke="#fff" stroke-width="2" fill="none" stroke-linecap="round"/></svg></div>
  <p class="abs body-copy feature-text" style="top:104px;">sed do eiusmod tempor incididunt ut labore et dolore magna aliqua. Ut enim ad minim veniam, quis nostrud exercitation ullamco laboris nisi ut aliquip ex ea commodo consequat.</p>

  <div class="abs photo-ring" style="left:22px;top:190px;width:86px;height:86px;"></div>
  <div class="abs photo photo--round" role="img" aria-label="Vet team caring for a dog" style="left:30px;top:198px;width:70px;height:70px;"></div>
  <div class="abs tick" style="left:18px;top:202px;"><svg width="12" height="12" viewBox="0 0 12 12"><path d="M2 6.5 L5 9 L10 3" stroke="#fff" stroke-width="2" fill="none" stroke-linecap="round"/></svg></div>
  <p class="abs body-copy feature-text" style="top:198px;">sed do eiusmod tempor incididunt ut labore et dolore magna aliqua. Ut enim ad minim veniam, quis nostrud exercitation ullamco laboris nisi ut aliquip ex ea commodo consequat.</p>

  <div class="abs photo-ring" style="left:22px;top:284px;width:86px;height:86px;"></div>
  <div class="abs photo photo--round" role="img" aria-label="Staff checking a shepherd dog" style="left:30px;top:292px;width:70px;height:70px;"></div>
  <div class="abs tick" style="left:18px;top:296px;"><svg width="12" height="12" viewBox="0 0 12 12"><path d="M2 6.5 L5 9 L10 3" stroke="#fff" stroke-width="2" fill="none" stroke-linecap="round"/></svg></div>
  <p class="abs body-copy feature-text" style="top:292px;">sed do eiusmod tempor incididunt ut labore et dolore magna aliqua. Ut enim ad minim veniam, quis nostrud exercitation ullamco laboris nisi ut aliquip ex ea commodo consequat.</p>

  <h3 class="abs heading white" style="left:20px;top:436px;width:200px;font-size:12.5px;">Lorem ipsum dolor sit amet, consectetur adipiscing</h3>
  <p class="abs body-copy white" style="left:20px;top:468px;width:200px;">sed do eiusmod tempor incididunt ut labore et dolore magna aliqua. Ut enim ad minim veniam, quis nostrud exercitation ullamco laboris nisi ut aliquip ex ea commodo consequat.</p>

  <!-- About panel -->
  <div class="abs blob" style="left:262px;top:28px;width:178px;height:142px;border:1.5px dashed var(--teal);"></div>
  <div class="abs blob photo" role="img" aria-label="Puppy and kitten playing together" style="left:272px;top:38px;width:158px;height:122px;border:5px solid var(--orange);background:linear-gradient(135deg,#f1efec,#c9c3bb);"></div>
  <h2 class="abs heading magenta about-title">About Us</h2>
  <p class="abs body-copy about-text">Lorem ipsum dolor sit amet, consectetur adipiscing elit, sed do eiusmod tempor incididunt ut labore et dolore magna aliqua. Ut enim ad minim veniam, quis nostrud exercitation ullamco laboris nisi ut aliquip ex ea commodo consequat.</p>
  <div class="abs" role="img" aria-label="Cream labrador puppy lying down" style="left:290px;top:298px;width:140px;height:74px;border-radius:40% 45% 20% 20%;background:linear-gradient(180deg,#f4efe6,#ddd2c2);"></div>
  <div class="abs contact">
    <svg width="8" height="10" viewBox="0 0 8 10"><path d="M4 0.5 A3.2 3.2 0 0 1 7.2 3.7 C7.2 6 4 9.5 4 9.5 C4 9.5 0.8 6 0.8 3.7 A3.2 3.2 0 0 1 4 0.5 Z" fill="none" stroke="var(--magenta)" stroke-width="1"/><circle cx="4" cy="3.7" r="1.1" fill="var(--magenta)"/></svg><br>
    address line 1, address line 1, address line 1,<br>address line 2.<br>
    <svg width="9" height="7" viewBox="0 0 9 7"><rect x="0.5" y="0.5" width="8" height="6" fill="none" stroke="var(--magenta)"/><path d="M0.5 0.5 L4.5 4 L8.5 0.5" fill="none" stroke="var(--magenta)"/></svg>hello@pawhavenclub.com<br>
    <svg width="8" height="8" viewBox="0 0 8 8"><circle cx="4" cy="4" r="3.5" fill="none" stroke="var(--magenta)"/><path d="M2.6 2.4 L3.4 2.2 L3.8 3.4 L3.2 3.8 C3.6 4.6 4 5 4.6 5.2 L5 4.6 L6 5 L5.8 5.8 C4 6 2.2 4.2 2.6 2.4 Z" fill="var(--magenta)"/></svg>0100 555 010<br>
    <svg width="8" height="8" viewBox="0 0 8 8"><circle cx="4" cy="4" r="3.5" fill="none" stroke="var(--magenta)"/><path d="M0.5 4 H7.5 M4 0.5 C2 2.5 2 5.5 4 7.5 M4 0.5 C6 2.5 6 5.5 4 7.5" fill="none" stroke="var(--magenta)" stroke-width="0.7"/></svg>www.pawhavenclub.com
  </div>

  <!-- Cover panel -->
  <h1 class="abs heading cover-title">dog<br>daycare</h1>
  <div class="abs blob" style="left:483px;top:128px;width:204px;height:176px;border:1.5px dashed var(--white);"></div>
  <div class="abs blob photo" role="img" aria-label="Woman hugging a white puppy" style="left:493px;top:138px;width:184px;height:156px;border:6px solid var(--magenta);"></div>
  <h2 class="abs heading magenta cover-tagline">dog daycare<br>and boarding</h2>
  <div class="abs cover-rule"></div>
  <svg class="abs" style="left:578px;top:404px;" width="12" height="12" viewBox="0 0 12 12" aria-hidden="true"><circle cx="6" cy="6" r="5.5" fill="var(--orange)" stroke="var(--white)"/><path d="M3.8 3.4 L5 3.1 L5.6 4.8 L4.8 5.4 C5.3 6.5 5.8 7 6.7 7.3 L7.2 6.5 L8.8 7 L8.6 8.3 C6 8.6 3.3 6 3.8 3.4 Z" fill="var(--white)"/></svg>
  <div class="abs cover-phone">0100 555 010</div>
  <div class="abs cover-web">www.pawhavenclub.com</div>
</section>

<!-- Inside spread -->
<section class="brochure brochure--inside">
  <svg class="brochure__bg" width="700" height="540" viewBox="0 0 700 540" aria-hidden="true">
    <rect x="0" y="0" width="233.3" height="540" fill="var(--yellow)"/>
    <rect x="233.3" y="0" width="233.4" height="540" fill="var(--orange)"/>
    <rect x="466.7" y="0" width="233.3" height="540" fill="var(--magenta)"/>
    <path d="M0 400 C80 385 150 432 233.3 440 L233.3 540 L0 540 Z" fill="var(--teal)"/>
    <path d="M0 400 C80 385 150 432 233.3 440" fill="none" stroke="var(--white)" stroke-width="1.2" stroke-dasharray="3 3" transform="translate(0 8)"/>
    <path d="M233.3 440 C310 445 400 420 466.7 350 L466.7 540 L233.3 540 Z" fill="var(--teal)"/>
    <path d="M233.3 440 C310 445 400 420 466.7 350" fill="none" stroke="var(--white)" stroke-width="1.2" stroke-dasharray="3 3" transform="translate(0 8)"/>
    <path d="M466.7 350 C530 290 610 300 700 282 L700 540 L466.7 540 Z" fill="var(--teal)"/>
    <path d="M466.7 350 C530 290 610 300 700 282" fill="none" stroke="var(--white)" stroke-width="1.2" stroke-dasharray="3 3" transform="translate(0 10)"/>
  </svg>

  <!-- Why us panel -->
  <div class="abs blob" style="left:12px;top:22px;width:212px;height:194px;border:1.5px dashed var(--teal);"></div>
  <div class="abs blob photo" role="img" aria-label="Happy terrier lying on green grass" style="left:22px;top:30px;width:192px;height:176px;border:6px solid var(--magenta);background:linear-gradient(135deg,#7fae4f,var(--photo-grass));"></div>
  <h2 class="abs heading magenta why-title">Why Us</h2>
  <div class="abs why-rule"></div>
  <p class="abs body-copy why-text">Lorem ipsum dolor sit amet, consectetur adipiscing elit, sed do eiusmod tempor incididunt ut labore et dolore magna aliqua. Ut enim ad minim veniam, quis nostrud exercitation ullamco laboris nisi ut aliquip ex ea commodo consequat. Duis aute irure dolor in reprehenderit in voluptate velit esse cillum dolore eu fugiat nulla pariatur.</p>
  <div class="abs photo" role="img" aria-label="Woman holding a white fluffy dog" style="left:80px;top:380px;width:72px;height:72px;border-radius:50%;border:4px solid var(--magenta);"></div>
  <div class="abs quote-mark" style="left:20px;top:458px;">&ldquo;</div>
  <p class="abs quote" style="left:48px;top:466px;width:170px;">sed do eiusmod tempor incididunt ut labore et dolore magna aliqua. Ut enim ad minim veniam, quis nostrud exercitation ullamco laboris nisi ut aliquip ex ea commodo consequat.</p>
  <div class="abs quote-author" style="left:140px;top:512px;">MARA LIND</div>
  <div class="abs quote-mark" style="left:190px;top:498px;">&rdquo;</div>

  <!-- Services panel -->
  <h2 class="abs heading services-title">OUR SERVICES</h2>
  <div class="abs services-rule"></div>
  <div class="abs service" style="top:62px;"><div class="photo" role="img" aria-label="Dogs in the indoor dog park"></div><span>Large Indoor<br>Dog Park</span></div>
  <div class="abs service" style="top:128px;"><div class="photo" role="img" aria-label="Dog swimming in a pool" style="background:linear-gradient(135deg,#3b8fd0,#1f5f9e);"></div><span>Swimming<br>Pools</span></div>
  <div class="abs service" style="top:194px;"><div class="photo" role="img" aria-label="Dogs in the daycare room"></div><span>Dog Daycare<br>and Boarding</span></div>
  <div class="abs service" style="top:260px;height:74px;border-bottom:none;"><div class="photo" role="img" aria-label="Dog training class outdoors" style="background:linear-gradient(135deg,#9cbf73,#d7d2c2);"></div><span>Pet Cpr/First Aid<br>Classes<br>And Training</span></div>
  <div class="abs photo" role="img" aria-label="Woman with a small dog among flowers" style="left:316px;top:372px;width:66px;height:66px;border-radius:50%;border:4px solid var(--magenta);background:linear-gradient(135deg,#8fbf5a,#e2a46a);"></div>
  <div class="abs quote-mark" style="left:250px;top:450px;">&ldquo;</div>
  <p class="abs quote" style="left:276px;top:456px;width:180px;">sed do eiusmod tempor incididunt ut labore et dolore magna aliqua. Ut enim ad minim veniam, quis nostrud exercitation ullamco laboris nisi ut aliquip ex ea commodo consequat.</p>
  <div class="abs quote-author" style="left:380px;top:502px;">MARA LIND</div>
  <div class="abs quote-mark" style="left:428px;top:488px;">&rdquo;</div>

  <!-- Pricing panel -->
  <h2 class="abs heading pricing-title">PRICING &amp;<br>MEMBERSHIP</h2>
  <div class="abs pricing-rule"></div>
  <div class="abs price-row" style="top:88px;">
    <span class="price-tag">$199</span><span class="price-name">Lorem ipsum</span>
    <p class="price-note">sed do eiusmod tempor incididunt ut labore et dolore magna aliqua. Ut enim ad minim veniam.</p>
  </div>
  <div class="abs price-row" style="top:156px;">
    <span class="price-tag">$199</span><span class="price-name">Lorem ipsum</span>
    <p class="price-note">sed do eiusmod tempor incididunt ut labore et dolore magna aliqua. Ut enim ad minim veniam.</p>
  </div>
  <div class="abs price-row" style="top:224px;">
    <span class="price-tag">$199</span><span class="price-name">Lorem ipsum</span>
    <p class="price-note">sed do eiusmod tempor incididunt ut labore et dolore magna aliqua. Ut enim ad minim veniam.</p>
  </div>
  <div class="abs blob" style="left:486px;top:316px;width:204px;height:206px;border:1.5px dashed var(--white);"></div>
  <div class="abs blob photo" role="img" aria-label="Woman giving a high five to a golden retriever indoors" style="left:496px;top:326px;width:184px;height:186px;border:6px solid var(--orange);background:linear-gradient(135deg,#f1ece4,#c89a6a);"></div>
</section>

</body>
</html>
```